Greek Souvlaki Restaurant Menu Design

We would like to redesign our menu (at the moment just a price-list without any graphics) and create something more fun.

You can find all the items we are offering at the following link / our e-shop:
https://olivebranchkitchen.example/orders/en/order/
I have also attached a printout of the above with hand written notes on the sections and items that will be included.

Our menu is divided to a couple of parts:
- Souvlaki Bar and Grill
- Authentic Greek Cuisine
- Wine List
- Desserts
- Bakaliko

This project will take on the first part of our menu, which is the Souvlaki Bar and Grill. If we are happy with your design, we will then develop the rest of our menu.

Souvlaki Bar and Grill
---------------------------

Our souvlaki can be customised to the customer requirements. The following links have similar set ups:

WOW!Patty
https://gr.pinboardly.example/pin/100000000000000001/
I like the way they have set it up, but the graphics and colours used are not my thing. I also like they way they have split up the steps, choose, top it of, etc.

The Krokk
https://gr.pinboardly.example/pin/100000000000000002/
I hate the step 1,2,3 on the left side. It does not make it playful. Like the fact that they have used pictures of the ingredients.

https://gr.pinboardly.example/pin/100000000000000003/
Hate the graphics, like the concept.

-------------

First Sections: Our Souvliaki Pita Wrap

The steps to customise a souvlaki can be found on the following link:
https://olivebranchkitchen.example/orders/en/order/ and choose pita wrap.

Most of the one side of our Souvliaki/Grill menu should be dedicated to our Pita Wraps.

It should have a small description of the Greek Souvlaki Pita Wrap. Something along the lines of "Get a whole meal all wrapped up with our delicious Greek Pita Wraps. Containing protein, sauce and salad". Improvements of this line are welcome.

It should then have the steps to customise it.

Step One.
Choose Base:
1. Chicken Skewer
2. Pork Skewer
3. etc
Price and options can be found on the above link on our website

Step Two.
Add one of our delicious home made sauces.
Options can be found on our website.

Step Three
Finalise it with the ingredients of your choice.
The customer can select multiple incredients

Step Four.
Feeling Hungry? Add extras:
Extras and Prices can be found on the link provided.

Buy two wraps and save. Takeaway only!
You will find this option as "Double Souvlaki Pita Wrap Offer."
Instead of 2x5.5 = £11 pay £10.5. This offer should also be mentioned somewhere on this section.

-----

Second Section - Our Platters

Skewers Platter and Gyros Platter

Options can be found by clicking on the items on the link provided.

Extras and Pita Bread option are common. Meat options are different and skewers have a choice of side. Meat options have 2/3 skewers and 200/300 grams of gyros, so they can probably be combined somehow.

These section can also be called Naked / Open Souvlaki Platters

Third Section
From Our Grill

All options from this section together with modifiers (can be see if you click on each item). I would like pictures from each item.

Forth Section
Meal Deals, starter combo and Set Menu.

Meal Deal for 1/2 and 4 are wraps with extras. The for 4 is not on the pdf and will be up on our website soon, so please check. I think those are easy to e incorporated next to the pita wrap section as upgrades to save.

Set menus are various items.

If they can fit on this page somehow we incorporate them, if not we can make a separate page with the offers / meals deals. If a separate page is created them the meal deal from our kitchen and vegetarean set menu should also be included.

Fifth Section
Salads and Starter

I would like all options from Hot and Cold starter and our salad. I would like pictures next to all options, if possible.

-----

Final notes/ideas.

Wraps, platters and grill could be one page front and back. Salads and starters could be a different page(s) or sections.

The menu should be easily updated and we would like a format where we can update prices and descriptions.

Prices and descriptions can be found on the link provided.

Feel free to improve our descriptions and titles. Please do mention where you made improvements, so we can approve them.

Our kitchen, dessert and wine menu will be given as a separate project and priority will be given to the person that won this competition.

If you need better quality pictures please let us know, most of the pictures we do have them in raw format too.

------

Some designs that I like. To give you an idea of the design I would like to see:

https://www.craftmarketly.example/listing/100000001/american-menu-restaurant-cafe-menus
I would love to see something like that for the grill/salad/starter side of our menu, since it has space for pictures.

https://gr.pinboardly.example/pin/100000000000000004/
I would love to see something like that, where the incredients of a souvlaki come together. This is optional and does not have to be there.

https://gr.pinboardly.example/pin/100000000000000005/

https://gr.pinboardly.example/pin/100000000000000006/

https://gr.pinboardly.example/pin/100000000000000007/

https://gr.pinboardly.example/pin/100000000000000008/

Target Market(s)

London

Font styles to use
Serif
Sans Serif

Colors
abd037
3277b5
33a6d7

Requirements
Must have
• Build your own souvlaki section. See description for examples.

Pictures for starters and salads.

Should be elegant
Nice to have
• Incorporate our relevant meal deals on the souvlaki pita section

```html
<!DOCTYPE html>
<html lang="en">
<head>
<meta charset="utf-8">
<title>Souvlaki Bar and Grill Menu</title>
<link href="https://fonts.googleapis.com/css2?family=Amatic+SC:wght@400;700&family=Oswald:wght@400;500&family=Open+Sans:wght@400;600;700&display=swap" rel="stylesheet">
<style>
:root{
  --navy:#0f4a78;
  --blue:#1a8fd0;
  --sky:#33a6d7;
  --green:#abd037;
  --gold:#f3b21a;
  --ink:#3a3a3a;
  --panel:#ededeb;
  --canvas:#f4f4f4;
  --white:#ffffff;
}
*{box-sizing:border-box;margin:0;padding:0}
html,body{width:1200px;height:600px;overflow:hidden;background:var(--canvas)}
body{position:relative;font-family:"Open Sans",sans-serif;color:var(--ink)}
.page{position:absolute;top:52px;width:753px;height:1063px;transform:scale(.4662);transform-origin:0 0;overflow:hidden;border:1px solid #d6d6d6}
.page--wraps{left:54px;background:var(--white)}
.page--deals{left:424px;background:var(--navy)}
.page--grill{left:795px;background:var(--white)}
.abs{position:absolute}
.hand{font-family:"Amatic SC",sans-serif;font-weight:700;line-height:1;color:var(--navy)}
.hand .hl{color:var(--blue)}
.photo{position:absolute}
.body{font-size:12.5px;line-height:14px}
.list{list-style:none;font-size:13px;line-height:20.3px}
.list li{white-space:nowrap}
.list li.two{height:24px;line-height:11px;padding-top:1px}
.plus{color:var(--blue)}
.veg{display:inline-block;width:10px;height:10px;border-radius:50%;background:var(--green);vertical-align:-1px;margin-left:2px}
.stack{display:inline-block;line-height:10px;vertical-align:top}
.step-num{display:inline-block;width:18px;height:18px;border-radius:50%;background:var(--blue);color:#fff;font:600 11px/18px "Open Sans",sans-serif;text-align:center}
.step-head{font-family:"Amatic SC",sans-serif;font-weight:700;font-size:19px;line-height:17px;color:var(--navy);white-space:nowrap}
.step-head .hl{color:var(--blue)}
.band{position:absolute;left:0;width:100%;height:12px;background:var(--blue);border-top:3px solid var(--sky);border-bottom:3px solid var(--sky)}
.extras{position:absolute;background:var(--blue);color:#fff;border-radius:46% 54% 50% 50% / 42% 48% 52% 58%}
.extras h4{font:700 27px/1 "Amatic SC",sans-serif;color:var(--navy)}
.extras ul{list-style:none;font:700 12.5px/18px "Open Sans",sans-serif;white-space:nowrap}
.extras b{color:var(--navy)}
.plat-title{font:700 34px/1 "Amatic SC",sans-serif;color:var(--navy);border-bottom:2px solid var(--blue);padding-bottom:4px;white-space:nowrap}
.plat-title .price{color:var(--blue);margin-left:8px}
.caption{font-size:10px;font-style:italic;font-weight:600;line-height:11px}
.row-line{position:absolute;height:2px;background:var(--blue)}
.count{font:700 26px/0.8 "Amatic SC",sans-serif;color:var(--navy);text-align:center}
.count small{display:block;font:400 14px/1 "Oswald",sans-serif;color:var(--blue)}
/* deals */
.deal-title{font:500 31px/1 "Oswald",sans-serif;color:#cfe3f3;white-space:nowrap;letter-spacing:-.5px}
.deal-title .for{color:var(--gold)}
.deal-title .price{margin-left:12px}
.deal-rail{position:absolute;left:63px;border-left:2px dotted var(--gold)}
.deal-line{position:absolute;left:75px;font:500 19px/1 "Oswald",sans-serif;color:#fff;white-space:nowrap;letter-spacing:-.4px}
.deal-note{position:absolute;left:75px;font-size:13.5px;color:#fff;white-space:nowrap}
.deal-list{position:absolute;left:75px;list-style:none;font-size:13.5px;line-height:20.3px;color:#fff;white-space:nowrap}
.side-panel{position:absolute;left:447px;top:22px;width:285px;height:1020px;background:var(--white)}
.side-rule{position:absolute;left:0;width:100%;height:6px;border-top:2px dotted var(--navy);border-bottom:2px dotted var(--navy)}
.side-title{position:absolute;left:33px;font:700 36px/1 "Amatic SC",sans-serif;color:var(--blue)}
.side-list{position:absolute;left:33px;list-style:none;font-size:13.5px;color:var(--ink);white-space:nowrap}
/* grill */
.dish-title{font:700 34px/1 "Amatic SC",sans-serif;color:var(--navy);white-space:nowrap}
.dish-title .price{color:var(--blue);margin-left:8px}
.dish-desc{font-size:11.5px;line-height:13.5px}
.dish-desc .side{color:var(--blue);font-weight:700}
.note{font:700 17px/18px "Amatic SC",sans-serif;color:var(--navy);white-space:nowrap}
.note .hl{color:var(--blue)}
.pointer{position:absolute;border-left:1.5px solid var(--sky)}
</style>
</head>
<body>

<!-- Page one: wraps and platters -->
<section class="page page--wraps">
  <div class="abs" style="left:330px;top:0;width:423px;height:490px;background:var(--panel)"></div>

  <h1 class="hand abs" style="left:65px;top:42px;font-size:40px;font-weight:400;line-height:31px;padding-bottom:6px;border-bottom:2px solid var(--blue);width:192px">SOUVLAKI<br>PITA WRAP <span class="hl" style="font-weight:700">£5.50</span></h1>
  <p class="body abs" style="left:65px;top:127px;width:190px">Get a whole meal all wrapped up with our delicious Greek Pita Wraps. Containing protein, sauce and salad.<br>It will leave you craving them time and time again.</p>

  <div class="photo" role="img" aria-label="Souvlaki pita wrap with fries and tomato in a paper sleeve" style="left:0;top:240px;width:325px;height:385px;background:linear-gradient(135deg,#5d8fbf 0%,#b9c7d3 45%,#c99a5e 75%,#5f8bb8 100%)"></div>

  <div class="abs" style="left:365px;top:85px">
    <span class="step-num" style="margin-left:9px">1</span>
    <div class="step-head" style="margin-top:4px">CHOOSE THE <span class="hl">BASE</span> YOU WANT :</div>
    <ul class="list" style="margin-top:6px">
      <li>Chicken <span class="plus">+</span> £0.50</li>
      <li>Pork <span class="plus">+</span> £0.50</li>
      <li>Gyros Chicken <span class="plus">+</span> £1.50</li>
      <li>Gyros Pork <span class="plus">+</span> £1.50</li>
      <li class="two"><span class="stack">Mixed Gyros<br>(Chicken and Pork)</span> <span class="plus">+</span> £2.00</li>
      <li class="two"><span class="stack">Kebab<br>(Lamb and Beef)</span> <span class="plus">+</span> £0.50</li>
      <li>Sausage <span class="plus">+</span> £0.50</li>
      <li>Haloumi <span class="veg"></span> <span class="plus">+</span> £0.50</li>
      <li>No Base <span class="veg"></span></li>
    </ul>
  </div>

  <div class="abs" style="left:570px;top:60px">
    <span class="step-num" style="margin-left:9px">2</span>
    <div class="step-head" style="margin-top:4px">ADD ONE OF OUR DELICIOUS<br><span class="hl">HOME MADE SAUCES</span> :</div>
    <ul class="list" style="line-height:18px;margin-top:4px">
      <li>Tzatziki <span class="veg"></span></li>
      <li>Tyrokafteri <span class="veg"></span></li>
      <li>Burger Sauce</li>
    </ul>
  </div>

  <div class="abs" style="left:541px;top:218px">
    <span class="step-num" style="margin-left:9px">3</span>
    <div class="step-head" style="margin-top:4px">FINALISE IT WITH THE<br><span class="hl">INGREDIENTS</span> OF YOUR CHOICE :</div>
    <ul class="list" style="line-height:18px;margin-top:4px">
      <li>Fries</li><li>Tomatoes</li><li>Onions</li>
    </ul>
  </div>

  <div class="abs" style="left:415px;top:365px;white-space:nowrap">
    <span class="step-num">4</span>
    <span class="step-head">IF YOU ARE FEELING <span class="hl">EXTRA</span> HUNGRY :</span>
  </div>
  <ul class="list abs" style="left:383px;top:391px">
    <li>Double Pita Bread <span class="plus">+</span> £1.00</li>
    <li>add Pork Skewer <span class="plus">+</span> £2.50</li>
    <li>add Chicken Skewer <span class="plus">+</span> £2.50</li>
  </ul>
  <ul class="list abs" style="left:570px;top:391px">
    <li class="two" style="height:20.3px"><span class="stack">add Kebab<br>(Lamb and Beef)</span> <span class="plus">+</span> £2.50</li>
    <li>add Sausage <span class="plus">+</span> £2.50</li>
    <li>add Haloumi <span class="plus">+</span> £1.90</li>
  </ul>

  <div class="abs" style="left:330px;top:490px;width:423px;height:137px;background:var(--navy);border-top:3px dotted var(--sky)"></div>
  <p class="abs" style="left:363px;top:513px;font:700 22px/24px 'Amatic SC',sans-serif;color:#fff;white-space:nowrap">Buy <span style="color:var(--sky)">2 WRAPS</span> and save!<br><span style="margin-left:10px">for </span><span style="color:var(--sky);font-size:28px">£10.50</span></p>
  <div class="abs" style="left:365px;top:568px;width:135px;height:36px;border:2px solid #fff;border-radius:18px;background:var(--white);color:var(--navy);font:700 26px/32px 'Amatic SC',sans-serif;text-align:center;white-space:nowrap">TAKEAWAY ONLY</div>
  <div class="photo" role="img" aria-label="Two souvlaki pita wraps side by side" style="left:535px;top:492px;width:205px;height:135px;border-radius:50% 50% 0 0 / 30% 30% 0 0;background:linear-gradient(120deg,#e9e6e0,#c79b62 50%,#e5e1da)"></div>

  <div class="band" style="top:627px"></div>

  <div class="extras" style="left:-10px;top:745px;width:195px;height:225px;padding:58px 0 0 40px">
    <h4 style="margin-left:14px">EXTRAS</h4>
    <ul style="margin-top:4px">
      <li>Extra Haloumi &nbsp;<b>£3.50</b></li>
      <li>Extra Tzatziki &nbsp;<b>£3.00</b></li>
      <li>1 Pita Bread &nbsp;<b>FREE</b></li>
      <li>2 Pita Breads &nbsp;<b>£1.00</b></li>
    </ul>
  </div>

  <div class="abs" style="left:227px;top:670px">
    <h2 class="plat-title">SKEWERS PLATTER<span class="price">£10.00</span></h2>
  </div>
  <div class="photo" role="img" aria-label="Chicken skewers on a plate with fries and salad" style="left:227px;top:711px;width:225px;height:125px;background:linear-gradient(180deg,#6f9cc7,#e8d2a2 55%,#c58a3c)"></div>
  <p class="caption abs" style="left:243px;top:839px;white-space:nowrap">Served with fries or salad and pita bread.</p>
  <div class="count abs" style="left:240px;top:870px;width:45px">2<small>skewers</small></div>
  <p class="body abs" style="left:305px;top:870px;font-size:13px;line-height:20px">Chicken / Pork /<br>Kebab (Lamb + Beef)</p>
  <div class="row-line" style="left:227px;top:913px;width:225px"></div>
  <div class="count abs" style="left:240px;top:922px;width:45px">3<small>skewers<br>+ £3.00</small></div>
  <p class="body abs" style="left:305px;top:922px;font-size:13px;line-height:20px">Chicken / Pork /<br>Kebab (Lamb + Beef)</p>
  <div class="row-line" style="left:227px;top:972px;width:225px"></div>
  <div class="count abs" style="left:240px;top:984px;width:45px;font-family:Oswald,sans-serif;font-size:19px;font-weight:500">SIDE<small>options</small></div>
  <p class="body abs" style="left:305px;top:980px;font-size:13px;line-height:20px">Fries<br>Side Salad <span class="plus">+</span> £2.50</p>

  <div class="abs" style="left:500px;top:670px">
    <h2 class="plat-title">GYROS PLATTER<span class="price">£13.00</span></h2>
  </div>
  <div class="photo" role="img" aria-label="Gyros platter with fries, tomatoes and onions" style="left:500px;top:711px;width:197px;height:125px;background:linear-gradient(180deg,#7ea3c6,#d9b27a 45%,#b4512f 80%,#e6ddd0)"></div>
  <p class="caption abs" style="left:500px;top:839px;width:200px">Served with refreshing tzatziki sauce, pita bread, fries, onion, tomatoes and lettuce.</p>
  <div class="count abs" style="left:496px;top:888px;font-family:Oswald,sans-serif;font-size:21px;font-weight:500">200<small>gr</small></div>
  <div class="abs" style="left:537px;top:875px;width:14px;height:58px;border:1.5px solid var(--blue);border-right:0"></div>
  <ul class="list abs" style="left:558px;top:866px">
    <li>Chicken Gyros</li>
    <li>Pork Gyros</li>
    <li class="two"><span class="stack">Mixed Gyros<br>(Chicken and Pork)</span> <span class="plus">+</span> £1.00</li>
  </ul>
  <div class="count abs" style="left:496px;top:970px;font-family:Oswald,sans-serif;font-size:21px;font-weight:500">300<small>gr</small></div>
  <div class="abs" style="left:537px;top:956px;width:14px;height:58px;border:1.5px solid var(--blue);border-right:0"></div>
  <ul class="list abs" style="left:558px;top:947px">
    <li>Chicken Gyros <span class="plus">+</span> £3.50</li>
    <li>Pork Gyros <span class="plus">+</span> £3.50</li>
    <li class="two"><span class="stack">Mixed Gyros<br>(Chicken and Pork)</span> <span class="plus">+</span> £4.50</li>
  </ul>
</section>

<!-- Page two: meal deals -->
<section class="page page--deals">
  <h2 class="deal-title abs" style="left:60px;top:66px">MEAL DEAL <span class="for">FOR 1</span><span class="price">£13.50</span></h2>
  <div class="deal-rail" style="top:108px;height:318px"></div>
  <div class="deal-line" style="top:108px">1 delicious PITA SOUVLAKI WRAP</div>
  <div class="deal-note" style="top:133px">can be individually customised to your taste.</div>
  <div class="deal-line" style="top:160px">1 our HEALTHY SALAD</div>
  <div class="deal-line" style="top:191px">1 SOFT DRINK</div>
  <div class="deal-line" style="top:222px">1 DESSERT</div>
  <ul class="deal-list" style="top:244px">
    <li>Loukoumades with Hazella (7) &nbsp;+ £2.00</li>
    <li>Loukoumades with Honey (7) &nbsp;+ £2.00</li>
    <li>Yogurt with Honey (small)</li>
    <li>Nut Cake in Syrup &nbsp;+ £2.00</li>
    <li>Orange Cake &nbsp;+ £2.00</li>
    <li>Galaktompoureko &nbsp;+ £2.00</li>
    <li>Baklava &nbsp;+ £2.00</li>
    <li style="line-height:14px;margin-top:3px">Halva Ice cream with Pistachio and<br>Chocolate &nbsp;+ £2.00</li>
  </ul>

  <h2 class="deal-title abs" style="left:60px;top:456px">MEAL DEAL <span class="for">FOR 2</span><span class="price">£24.00</span></h2>
  <div class="deal-rail" style="top:498px;height:136px"></div>
  <div class="deal-line" style="top:498px">2 delicious PITA SOUVLAKI WRAPS</div>
  <div class="deal-note" style="top:523px">can be individually customised to your taste.</div>
  <div class="deal-line" style="top:550px">1 our HEALTHY SALAD</div>
  <div class="deal-line" style="top:581px">2 SOFT DRINKS</div>
  <div class="deal-line" style="top:612px">1 DESSERT</div>

  <h2 class="deal-title abs" style="left:60px;top:668px">FAMILY MEAL DEAL <span class="for">FOR 4</span><span class="price">£45.00</span></h2>
  <div class="deal-rail" style="top:710px;height:286px"></div>
  <div class="deal-line" style="top:710px">4 delicious PITA SOUVLAKI WRAPS</div>
  <div class="deal-note" style="top:735px">can be individually customised to your taste.</div>
  <div class="photo" role="img" aria-label="Family spread of wraps, dips and salad" style="left:75px;top:763px;width:187px;height:130px;background:linear-gradient(135deg,#6d8fb2,#d9c7a4 40%,#c8783e 70%,#8aa6c0)"></div>
  <div class="deal-line" style="left:276px;top:763px">2 STARTERS</div>
  <ul class="deal-list" style="left:276px;top:785px">
    <li>Tzatziki <span class="veg" style="background:var(--gold)"></span></li>
    <li>Hummus</li>
    <li>White Taramosalata</li>
    <li>Fries <span class="veg"></span></li>
    <li>Fava</li>
  </ul>
  <div class="deal-line" style="top:906px">1 our HEALTHY SALAD</div>
  <div class="deal-line" style="top:937px">2 SOFT DRINKS</div>
  <div class="deal-line" style="top:968px">2 DESSERTS</div>
  <div class="deal-line" style="left:276px;top:906px">PITA BREAD</div>
  <ul class="deal-list" style="left:276px;top:928px">
    <li>1 x Pita</li>
    <li>2 x Pita &nbsp;+ £1.00</li>
  </ul>

  <div class="side-panel">
    <h3 class="side-title" style="top:68px">SALAD</h3>
    <ul class="side-list" style="top:118px;line-height:28px">
      <li>Side Salad</li>
      <li>Greek Salad &nbsp;+ £3.00</li>
      <li>Greek Salad No Onions &nbsp;+ £3.00</li>
      <li>Caesar Salad &nbsp;+ £4.50</li>
      <li>Olive Grove House Salad &nbsp;+ £4.00</li>
      <li style="line-height:14px;margin-top:6px">Olive Grove House Salad<br>with Prosciutto &nbsp;+ £5.00</li>
    </ul>
    <div class="side-rule" style="top:306px"></div>
    <h3 class="side-title" style="top:350px">SOFT DRINK</h3>
    <ul class="side-list" style="top:398px;line-height:20.3px">
      <li>Kola Fresca</li>
      <li>Kola Fresca Diet</li>
      <li>Kola Fresca Zero</li>
      <li>Lemoni Lemonade</li>
      <li>Lemoni Orange</li>
      <li>Applefizz</li>
      <li>Lymon</li>
      <li>Still Water (small)</li>
      <li>Sparkling Mineral Water (small)</li>
    </ul>
    <div class="side-rule" style="top:610px"></div>
    <h3 class="side-title" style="top:658px">DESSERTS</h3>
    <ul class="side-list" style="top:705px;line-height:28px">
      <li>Loukoumades with Hazella (7)</li>
      <li>Loukoumades with Honey (7)</li>
      <li>Yogurt with Honey</li>
      <li>Bougatsa</li>
      <li>Nut Cake in Syrup</li>
      <li>Orange Cake &nbsp;+ £0.50</li>
      <li>Sokolatopita &nbsp;+ £1.00</li>
      <li>Galaktompoureko &nbsp;+ £1.00</li>
      <li>Baklava &nbsp;+ £1.50</li>
      <li style="line-height:14px;margin-top:6px">Halva Ice cream with Pistachio<br>and Chocolate &nbsp;+ £1.00</li>
    </ul>
  </div>
</section>

<!-- Page three: grill and set menu -->
<section class="page page--grill">
  <div class="photo" role="img" aria-label="Grilled fillets with fries on a white plate" style="left:50px;top:62px;width:172px;height:125px;background:linear-gradient(135deg,#6b9ac6,#f0e2b8 45%,#c07a3a 70%,#7ea5cc)"></div>
  <div class="abs" style="left:235px;top:66px">
    <h2 class="dish-title">FILLETS<span class="price">£13.00</span></h2>
    <p class="dish-desc" style="width:160px;margin-top:6px">Grilled tender pork or chicken fillets topped with an oregano and lemon sauce. Served with fries.<br><span class="side">Side Salad &nbsp;+ £2.50</span></p>
  </div>

  <div class="photo" role="img" aria-label="Lamb cutlets with fries" style="left:50px;top:216px;width:172px;height:125px;background:linear-gradient(135deg,#6b9ac6,#f2df9c 40%,#7a4a2c 70%,#7ea5cc)"></div>
  <div class="abs" style="left:235px;top:220px">
    <h2 class="dish-title">LAMB CUTLETS</h2>
    <h2 class="dish-title" style="margin-left:8px"><span class="price" style="margin:0">£16.00</span></h2>
    <p class="dish-desc" style="width:150px;margin-top:10px">Tender lamb cutlets grilled to perfection and served with fries.<br><span class="side">Side Salad &nbsp;+ £2.50</span></p>
  </div>

  <div class="photo" role="img" aria-label="Village sausages with fries" style="left:50px;top:370px;width:172px;height:142px;background:linear-gradient(135deg,#6b9ac6,#f2df9c 40%,#9a3a2a 70%,#7ea5cc)"></div>
  <div class="abs" style="left:235px;top:374px">
    <h2 class="dish-title">VILLAGE SAUSAGES</h2>
    <h2 class="dish-title" style="margin-left:10px"><span class="price" style="margin:0">£9.50</span></h2>
    <p class="dish-desc" style="width:160px;margin-top:10px">Two large grilled sausages from Thrace served with mustard or lemon dressing. Served with fries.<br><span class="side">Side Salad &nbsp;+ £2.50</span></p>
  </div>

  <div class="abs" style="left:432px;top:66px">
    <h2 class="dish-title">SIRLOIN STEAK<span class="price">£24.50</span></h2>
    <p class="dish-desc" style="width:272px;margin-top:6px;text-align:justify">350gr Juicy Sirloin Steak! This highly desired cut of meat has a <b>beefier flavour, less fat and medium tender</b>, as it comes from an area where muscles get more exercise. We recommend it to be enjoyed medium cooked.</p>
  </div>
  <div class="photo" role="img" aria-label="Grilled steak with Greek salad" style="left:432px;top:188px;width:272px;height:163px;background:linear-gradient(110deg,#eeeae4,#5a3a2c 30%,#4a2e22 55%,#d9c9a8 75%,#b43a2a)"></div>
  <div class="abs" style="left:432px;top:374px">
    <h2 class="dish-title">RIBEYE STEAK<span class="price">£24.50</span></h2>
    <p class="dish-desc" style="width:272px;margin-top:6px;text-align:justify">350gr Juicy Rib-Eye Steak! This highly desired cut of meat has <b>full flavour, soft and rich texture and juicy finish</b>. We recommend it to be enjoyed medium cooked.</p>
  </div>

  <div class="abs" style="left:0;top:578px;width:100%;height:485px;background:var(--panel)"></div>
  <div class="band" style="top:566px"></div>

  <div class="extras" style="left:455px;top:485px;width:207px;height:200px;padding:52px 0 0 50px">
    <h4 style="margin-left:14px">EXTRAS</h4>
    <ul style="margin-top:4px">
      <li>Extra Haloumi &nbsp;<b>£3.50</b></li>
      <li>Extra Tzatziki &nbsp;<b>£3.00</b></li>
      <li>1 Pita Bread &nbsp;<b>FREE</b></li>
      <li>2 Pita Breads &nbsp;<b>£1.00</b></li>
    </ul>
  </div>

  <h2 class="hand abs" style="left:70px;top:612px;font-size:35px;text-align:center;line-height:29px;white-space:nowrap">SET MENU<br>FOR 2+ PEOPLE</h2>
  <div class="abs" style="left:72px;top:674px;width:145px;height:2px;background:var(--blue)"></div>
  <div class="abs" style="left:85px;top:678px;font:500 31px/1 'Oswald',sans-serif;color:var(--navy)">£60.00</div>

  <p class="note abs" style="left:65px;top:750px;text-align:center">FEELING HUNGRY?<br>GIVE OUR <span class="hl">BEST SELLING<br>GRILL ITEMS</span> A TRY :</p>
  <p class="note abs" style="left:68px;top:825px;line-height:20.3px">&nbsp;2 X CHICKEN SKEWERS<br>2 X PORK SKEWERS<br>2 X LAMB CUTLET PIECES<br>&nbsp;2 X HALOUMI<br>&nbsp;1 X VILLAGE SAUSAGE<br>&nbsp;CHICKEN FILLETS<br>PORK FILLETS<br>&nbsp;FRIES</p>

  <p class="note abs" style="left:252px;top:688px">MARINATED KALAMATA GIANT OLIVES</p>
  <p class="note abs" style="left:258px;top:710px">TZATZIKI</p>
  <p class="note abs" style="left:358px;top:710px">TYROKAFTERI</p>
  <div class="pointer" style="left:285px;top:728px;height:22px"></div>
  <div class="pointer" style="left:333px;top:706px;height:44px"></div>
  <div class="pointer" style="left:382px;top:728px;height:22px"></div>

  <div class="photo" role="img" aria-label="Mixed grill platter with dips, dessert and Greek salad" style="left:210px;top:743px;width:420px;height:270px;background:linear-gradient(135deg,#3f4e63,#d7c6a5 25%,#8a5a34 50%,#c78c44 70%,#e9e6e1 85%,#4a5f7a)"></div>

  <p class="note abs" style="left:644px;top:776px">YOUR CHOICE<br>OF DESSERT</p>
  <p class="note abs" style="left:644px;top:922px">YOUR CHOICE OF<br>SALAD</p>
  <div class="pointer" style="left:640px;top:815px;height:40px;transform:rotate(30deg)"></div>
  <div class="pointer" style="left:625px;top:915px;height:30px;transform:rotate(-50deg)"></div>
</section>

</body>
</html>
```